Tamaru Peruvian Cuisine needs a take-out menu

We need a new tri-fold 8.5"x11" take out menu for a Peruvian restaurant based in New Rochelle, NY. We have a vast selections of dishes from appetizers, seafood based dishes, desserts, Peruvian ceviches and more. We have attached the following:

Restaurant information
Pictures of our dishes
Tamaru Logo in pdf format
Menu in word format
Old take out menu for reference only! (our dishes have changed)
Updates

Project Deadline Extended
Reason: Need more time to make final decision.

Industry/Entity Type

Restaurant

```html
<!DOCTYPE html>
<html lang="en">
<head>
<meta charset="utf-8">
<title>Tamaru Peruvian Cuisine – Take-out Menu</title>
<link rel="stylesheet" href="https://fonts.googleapis.com/css2?family=Lora:wght@400;500&family=Open+Sans:ital,wght@0,400;1,400&family=Rosarivo&display=swap">
<style>
  :root {
    --wood-dark: #3e2headed;
    --wood: #5a3620;
    --wood-mid: #6b4128;
    --wood-deep: #45281a;
    --band: #36200f;
    --panel: #3a2314;
    --green: #7cc144;
    --banner-green: #4db34f;
    --banner-green-dark: #2f8a3c;
    --pill: #f6ebc6;
    --pill-border: #3a2212;
    --header-text: #2fb14c;
    --cream: #f4e3b6;
    --white: #ffffff;
    --desc: #f1e9de;
  }
  * { box-sizing: border-box; margin: 0; padding: 0; }
  html, body { width: 1200px; height: 848px; overflow: hidden; background: #2a170c; }
  .menu {
    position: relative; width: 1200px; height: 848px; overflow: hidden;
    background:
      linear-gradient(90deg, rgba(0,0,0,0.12) 0, rgba(0,0,0,0) 6%, rgba(0,0,0,0) 94%, rgba(0,0,0,0.15) 100%),
      linear-gradient(180deg, #5e3a22 0%, #56331d 30%, #61402a 55%, #50301c 80%, #5a3720 100%);
    font-family: "Lora", serif;
    color: var(--white);
  }
  .fold { position: absolute; top: 0; width: 1px; height: 848px; background: rgba(0,0,0,0.25); }
  .column { position: absolute; top: 0; height: 848px; }
  .col-left { left: 0; width: 395px; }
  .col-middle { left: 395px; width: 401px; }
  .col-right { left: 796px; width: 404px; }

  .banner { position: absolute; width: 212px; height: 62px; transform: translate(-50%, -50%); }
  .banner svg { position: absolute; inset: 0; }
  .banner span {
    position: absolute; inset: 0; display: flex; align-items: center; justify-content: center;
    font-family: "Rosarivo", serif; font-size: 17px; letter-spacing: 0.5px; color: var(--header-text);
  }
  .band {
    position: absolute; left: 0; width: 395px; height: 26px; background: var(--band);
    display: flex; align-items: center; justify-content: center;
    font-family: "Rosarivo", serif; font-size: 17px; color: var(--cream); letter-spacing: 0.5px;
  }

  .price, .name, .desc, .variant { position: absolute; white-space: nowrap; line-height: 1; }
  .price { font-size: 12.5px; color: var(--white); }
  .name { font-size: 14px; color: var(--green); }
  .desc { font-family: "Open Sans", sans-serif; font-style: italic; font-size: 9.6px; color: var(--desc); line-height: 12px; white-space: normal; }
  .variant { font-size: 11.5px; color: var(--green); }
  .variant b { font-weight: 400; color: var(--white); font-size: 12.5px; margin-left: 6px; }

  .photo { position: absolute; }
  .photo-dishes { left: 34px; top: 0; width: 323px; height: 129px; border-radius: 0 0 40px 40px;
    background: radial-gradient(ellipse at 50% 55%, #c9824a 0%, #e9dfcf 45%, rgba(235,228,215,0.0) 75%); }
  .photo-dessert { left: 279px; top: 605px; width: 122px; height: 230px; border-radius: 60px 0 0 60px;
    background: radial-gradient(ellipse at 60% 50%, #d88a3c 0%, #b9611f 55%, rgba(120,60,20,0) 85%); }

  .title { position: absolute; left: 0; width: 404px; text-align: center; font-family: "Rosarivo", serif;
    font-size: 31px; color: var(--cream); line-height: 1.33; top: 37px; }
  .frame { position: absolute; left: 28px; top: 148px; width: 350px; height: 244px; background: #5b3518;
    border: 3px solid #3d220f; box-shadow: inset 0 0 0 6px #7a4a22; }
  .frame .photo { left: 11px; top: 14px; width: 322px; height: 213px;
    background: linear-gradient(180deg, #c8d2d4 0%, #8fa08a 40%, #6b7a4c 65%, #8a8266 100%); }
  .brand { position: absolute; left: 210px; top: 383px; width: 150px; height: 78px; transform: translate(-50%, -50%);
    background: var(--pill); border: 4px solid var(--pill-border); border-radius: 50%;
    box-shadow: 0 0 0 4px var(--banner-green);
    display: flex; align-items: center; justify-content: center;
    font-family: "Lora", serif; font-size: 20px; color: var(--header-text); }

  .contact { position: absolute; left: 107px; font-family: "Rosarivo", serif; font-size: 24px; color: var(--white); line-height: 43px; }
  .icon { position: absolute; left: 70px; }

  .delivery { position: absolute; left: 0; top: 716px; width: 404px; height: 132px; background: var(--panel); text-align: center; }
  .delivery h2 { font-family: "Rosarivo", serif; font-weight: 400; font-size: 18px; color: var(--white); margin-top: 23px; letter-spacing: 0.3px; }
  .delivery p { font-family: "Open Sans", sans-serif; font-size: 12.6px; color: var(--desc); line-height: 26px; margin-top: 12px; }
</style>
</head>
<body>
<main class="menu">
  <div class="fold" style="left:395px"></div>
  <div class="fold" style="left:796px"></div>

  <!-- Left panel -->
  <section class="column col-left">
    <div class="banner" style="left:201px; top:53px">
      <svg width="212" height="62" viewBox="0 0 212 62"><path d="M0 18 L22 18 L22 44 L0 44 L8 31 Z M212 18 L190 18 L190 44 L212 44 L204 31 Z" fill="var(--banner-green)"/><rect x="14" y="3" width="184" height="56" rx="28" fill="var(--pill-border)"/><rect x="19" y="8" width="174" height="46" rx="23" fill="var(--pill)" stroke="var(--banner-green)" stroke-width="2"/></svg>
      <span>SEAFOOD</span>
    </div>

    <span class="price" style="left:14px; top:107px">$19.95</span><span class="name" style="left:69px; top:106px">Pescado A Lo Macho</span>
    <p class="desc" style="left:85px; top:124px; width:300px">fried fish fillet topped with seafood in hot yellow pepper sauce, served with rice and yuccas</p>
    <span class="price" style="left:14px; top:150px">$16.95</span><span class="name" style="left:69px; top:149px">Pescado Sudado</span>
    <p class="desc" style="left:85px; top:167px; width:300px">corvina fish stew, in hot yellow pepper, tomatoes, onions, served with yuccas and rice</p>
    <span class="price" style="left:14px; top:192px">$17.95</span><span class="name" style="left:69px; top:191px">Arroz Con Mariscos</span>
    <p class="desc" style="left:85px; top:213px; width:300px">peruvian style paella, red rice served with seafood</p>
    <span class="name" style="left:69px; top:234px">Arroz Chaufa</span>
    <p class="desc" style="left:85px; top:256px; width:310px">peruvian style fried rice served with choice of seafood or shrimp</p>
    <span class="variant" style="left:84px; top:287px">Mariscos<b>$17.95</b></span>
    <span class="variant" style="left:197px; top:287px">Camarones<b>$17.95</b></span>
    <span class="price" style="left:14px; top:321px">$26.95</span><span class="name" style="left:69px; top:320px">Trucha Frita</span>
    <p class="desc" style="left:85px; top:336px; width:290px">deep fried Trout, served with white rice, fried yuccas and salsa criolla</p>
    <span class="price" style="left:14px; top:364px">$30.95</span><span class="name" style="left:69px; top:363px">Jalea</span>
    <p class="desc" style="left:85px; top:386px; width:300px">deep fried mixed seafood and fish, served with fried yuccas</p>
    <span class="variant" style="left:84px; top:414px">Large<b>$28.95</b></span>
    <span class="variant" style="left:197px; top:414px">Small<b>$17.95</b></span>

    <div class="band" style="top:463px">SALADS</div>
    <span class="price" style="left:14px; top:506px">$6.95</span><span class="name" style="left:59px; top:505px">Ensalada de la Casa</span>
    <p class="desc" style="left:82px; top:528px; width:300px">lettuce, tomatoes, yellow peppers and zucchini</p>
    <span class="price" style="left:14px; top:550px">$7.95</span><span class="name" style="left:59px; top:549px">Ensalad Tamaru</span>
    <p class="desc" style="left:82px; top:565px; width:290px">lettuce, tomatoes, cucumbers, red onions, carrots, radish and avocado</p>
    <span class="price" style="left:14px; top:592px">$8.95</span><span class="name" style="left:59px; top:591px">Ensalada Cesar</span>
    <p class="desc" style="left:82px; top:609px; width:280px">romaine, lettuce, croutons, parmesan cheese and Tamaru's special sauce</p>

    <div class="band" style="top:658px">SIDES</div>
    <span class="price" style="left:16px; top:703px">$3.95</span><span class="name" style="left:59px; top:702px">Papas Fritas</span>
    <p class="desc" style="left:82px; top:723px">french fries</p>
    <span class="price" style="left:16px; top:746px">$3.95</span><span class="name" style="left:59px; top:745px">Arroz Blanco o Amarillo</span>
    <p class="desc" style="left:82px; top:767px">white/yellow rice</p>
    <span class="price" style="left:16px; top:789px">$3.95</span><span class="name" style="left:59px; top:788px">Frejoles</span>
    <p class="desc" style="left:82px; top:808px">peruvian canario beans</p>
    <span class="price" style="left:223px; top:703px">$3.95</span><span class="name" style="left:267px; top:702px">Maduros</span>
    <p class="desc" style="left:289px; top:723px">sweet plantains</p>
    <span class="price" style="left:223px; top:746px">$3.95</span><span class="name" style="left:267px; top:745px">Tostones</span>
    <p class="desc" style="left:263px; top:767px">fried green plantains</p>
    <span class="price" style="left:223px; top:789px">$3.95</span><span class="name" style="left:267px; top:788px">Yuca Frita</span>
    <p class="desc" style="left:289px; top:808px">fried yuccas</p>
  </section>

  <!-- Middle panel -->
  <section class="column col-middle">
    <div class="photo photo-dishes" role="img" aria-label="Platters of fried rice, roast chicken, salad and fries with dipping sauces"></div>
    <div class="banner" style="left:200px; top:165px">
      <svg width="212" height="62" viewBox="0 0 212 62"><path d="M0 18 L22 18 L22 44 L0 44 L8 31 Z M212 18 L190 18 L190 44 L212 44 L204 31 Z" fill="var(--banner-green)"/><rect x="14" y="3" width="184" height="56" rx="28" fill="var(--pill-border)"/><rect x="19" y="8" width="174" height="46" rx="23" fill="var(--pill)" stroke="var(--banner-green)" stroke-width="2"/></svg>
      <span>CHICKEN</span>
    </div>

    <span class="price" style="left:11px; top:224px">$6.50</span><span class="name" style="left:66px; top:223px">1/4 Pollo</span>
    <p class="desc" style="left:82px; top:244px">quarter chicken, served with two sides</p>
    <span class="price" style="left:11px; top:267px">$8.95</span><span class="name" style="left:66px; top:266px">1/2 Pollo</span>
    <p class="desc" style="left:82px; top:288px">half chicken, served with two sides</p>
    <span class="price" style="left:11px; top:310px">$16.95</span><span class="name" style="left:66px; top:309px">1 Pollo</span>
    <p class="desc" style="left:82px; top:330px">whole chicken, served with two sides</p>
    <span class="price" style="left:11px; top:352px">$20.95</span><span class="name" style="left:66px; top:351px">Pollo Limeno</span>
    <p class="desc" style="left:82px; top:368px; width:300px">whole chicken, served with French fries, avocado salad and yellow rice</p>
    <span class="price" style="left:11px; top:395px">$26.95</span><span class="name" style="left:66px; top:394px">Pollo Chalaco</span>
    <p class="desc" style="left:82px; top:411px; width:300px">whole chicken, served with avocado salad, salchipapa and yellow rice</p>
    <span class="price" style="left:11px; top:438px">$30.95</span><span class="name" style="left:66px; top:437px">Pollo Tamaru</span>
    <p class="desc" style="left:82px; top:454px; width:310px">whole chicken, served with avocado salad, arroz chaufa (chicken or steak) and salchipapa</p>

    <div class="banner" style="left:200px; top:539px">
      <svg width="212" height="62" viewBox="0 0 212 62"><path d="M0 18 L22 18 L22 44 L0 44 L8 31 Z M212 18 L190 18 L190 44 L212 44 L204 31 Z" fill="var(--banner-green)"/><rect x="14" y="3" width="184" height="56" rx="28" fill="var(--pill-border)"/><rect x="19" y="8" width="174" height="46" rx="23" fill="var(--pill)" stroke="var(--banner-green)" stroke-width="2"/></svg>
      <span>DESSERTS</span>
    </div>

    <div class="photo photo-dessert" role="img" aria-label="Golden fried picarones doughnuts"></div>
    <span class="price" style="left:11px; top:601px">$5.95</span><span class="name" style="left:66px; top:600px">Crema Volteada</span>
    <p class="desc" style="left:88px; top:622px">Peruvian caramel custard</p>
    <span class="price" style="left:11px; top:645px">$5.95</span><span class="name" style="left:66px; top:644px">Tres Leches</span>
    <p class="desc" style="left:88px; top:666px">Butter cake soaked in three kinds of milk</p>
    <span class="price" style="left:11px; top:687px">$5.95</span><span class="name" style="left:66px; top:686px">Torta Helada</span>
    <p class="desc" style="left:88px; top:708px">Sponge cake topped with strawberry jello</p>
    <span class="price" style="left:11px; top:730px">$5.95</span><span class="name" style="left:66px; top:729px">Torta de Chochoolate</span>
    <p class="desc" style="left:88px; top:751px">Chocolate cake</p>
    <span class="price" style="left:11px; top:773px">$5.95</span><span class="name" style="left:66px; top:772px">Picarones</span>
    <p class="desc" style="left:88px; top:791px; width:190px">Peruvian style sweet potato doughnut covered with syrup</p>
  </section>

  <!-- Right panel -->
  <section class="column col-right">
    <h1 class="title">Authentic<br>Peruvian Cuisine</h1>
    <div class="frame">
      <div class="photo" role="img" aria-label="Mountain ruins of the Andes under misty peaks"></div>
    </div>
    <div class="brand">Tamaru</div>

    <svg class="icon" style="top:478px" width="16" height="24" viewBox="0 0 16 24"><path d="M8 0C3.6 0 0 3.5 0 7.9 0 13.8 8 24 8 24s8-10.2 8-16.1C16 3.5 12.4 0 8 0zm0 11a3.2 3.2 0 1 1 0-6.4A3.2 3.2 0 0 1 8 11z" fill="var(--banner-green)"/></svg>
    <p class="contact" style="top:468px">218 HARBOR AVE. NEW<br>ROCHELLE, NY<br>10801</p>

    <svg class="icon" style="top:633px" width="22" height="22" viewBox="0 0 24 24"><path d="M6.6 10.8a15.1 15.1 0 0 0 6.6 6.6l2.2-2.2c.3-.3.7-.4 1-.2 1.1.4 2.3.6 3.6.6.6 0 1 .4 1 1V20c0 .6-.4 1-1 1A17 17 0 0 1 3 4c0-.6.4-1 1-1h3.5c.6 0 1 .4 1 1 0 1.3.2 2.5.6 3.6.1.3 0 .7-.2 1z" fill="var(--banner-green)"/></svg>
    <p class="contact" style="top:623px">914 555 0172</p>

    <div class="delivery">
      <h2>DELIVERY HOURS&nbsp; 11:30 AM – 10 PM</h2>
      <p>Deliveries on order of $15 or more, $5 fee for 3 miles<br>or more Chef's specials on weekends.</p>
    </div>
  </section>
</main>
</body>
</html>
```